maple lash nook

need a flyer for a brow bar and lash extensions bar, will send what I need and also have a beautiful lash extension picture on my website www.polishonparade.org to use... and black/white picture..
front page with logo
OPENING SPECIALS
Lid Tango: Over your brows? Had a dodge job? Our trained staff are here to get your brows back on track! Service includes: Total brow reshape, calming forehead and eyebrow Indian massage, soothing rosewater eye gel application, brow finish with complimentary brow makeup.
$18.00

Arches by the Harbour: Perfectly sculpted, arched and groomed? Check! Get the most gorgeous brows ever!
Service includes: brow gossip, brow shape, brow colour, calming forehead and eyebrow Indian massage, soothing rosewater eye gel application, and brow finish with
complimentary brow makeup. 
$25.00

Brows for Teens: Stand out at school for the right reason! No more mono-brow! Quick, thorough tidy, designed to suit your face. For students up to year 12.
$14.00

Brows for Men: Men, let’s be honest. Big Bushy Brows CAN be embarrassing. That’s where we come in. If you’re after a total reshape or just sick of that mono-brow, we’ll give you the look you’re after. There’s never too little or too much we can do to help!
$15.00

CALL NOW!
ASHGROVE 47261839
WILLOWBANKS 47285106

A division of
back page with logo

DID YOU KNOW THAT LONG,THICK
NATURAL-LOOKING EYELASHES CAN MAKE YOUR EYES APPEAR WIDER AND YOUR FACE MORE YOUTHFUL?

Price List
Natural lashes Full Set $99 (60 lashes each eye)
Celebrity Lashes Full Set $120 (80 lashes each eye)
Semi-set 1/2 eye $75 (30 lashes each eye)

Removal with Re-Application $15
Maintenance 2 weeks $40 (Max 8 lashes each eye)
Maintenance 3 weeks $55 (Max 12 Lashes each eye)
Maintenance Overdue $75 (Max 30 Lashes each eye)

Forget the hassle of tinting and mascara ,a visit to Polish on Parade will instantly revitalise your look with an under-stated and natural-looking glamour.

Call us today!
ASHGROVE 47261839
WILLOWBANKS 47285106

• red/white/black

```html
<!DOCTYPE html>
<html lang="en">
<head>
<meta charset="utf-8">
<title>maple lash nook – Opening Specials</title>
<link rel="stylesheet" href="https://fonts.googleapis.com/css2?family=Questrial&family=Didact+Gothic&display=swap">
<style>
  :root {
    --red-bright: #c4121a;
    --red-deep: #7a0a10;
    --red-dark: #3a0508;
    --black: #0b0b0b;
    --band-grey: #d9dcdc;
    --white: #ffffff;
    --ink-on-photo: #1a1a1a;
  }
  html, body {
    margin: 0;
    padding: 0;
    width: 927px;
    height: 1200px;
    overflow: hidden;
    background: var(--black);
  }
  .flyer {
    position: relative;
    width: 927px;
    height: 1200px;
    overflow: hidden;
    font-family: "Questrial", "Didact Gothic", sans-serif;
    color: var(--white);
    background:
      radial-gradient(ellipse 70% 55% at 70% 30%, rgba(210,40,50,0.55), transparent 70%),
      linear-gradient(180deg, #a3121a 0%, #8a0c14 35%, var(--red-dark) 70%, #120203 100%);
  }
  .side-band {
    position: absolute;
    left: 0; top: 0;
    width: 100px; height: 992px;
    background: linear-gradient(180deg, var(--red-bright) 0%, var(--red-deep) 45%, var(--red-dark) 75%, #160204 100%);
  }
  .side-rule {
    position: absolute;
    left: 100px; top: 0;
    width: 11px; height: 992px;
    background: var(--band-grey);
  }
  .side-title {
    position: absolute;
    left: 51px; top: 58px;
    transform-origin: 0 0;
    transform: rotate(90deg) translateY(-50%);
    white-space: nowrap;
    font-size: 41px;
    line-height: 1;
    letter-spacing: 0.3px;
  }
  .headline {
    position: absolute;
    left: 131px; top: 58px;
    margin: 0;
    font-size: 38px;
    font-weight: 400;
    line-height: 1.1;
    letter-spacing: 0.3px;
    white-space: nowrap;
  }
  .service {
    position: absolute;
    margin: 0;
    font-size: 24px;
    line-height: 32.7px;
    white-space: nowrap;
    z-index: 2;
  }
  .service strong { font-weight: 700; }
  .rehab { left: 135px; top: 122px; }
  .city  { left: 554px; top: 118px; }
  .teens { left: 129px; top: 674px; }
  .men   { left: 554px; top: 604px; }
  .on-photo { color: var(--ink-on-photo); }
  .lash-photo {
    position: absolute;
    left: 110px; top: 447px;
    width: 355px; height: 226px;
    background: linear-gradient(135deg, #f4f4f4 0%, #d9d9d9 45%, #8a6a52 70%, #e8e8e8 100%);
    z-index: 1;
  }
  .footer-rule {
    position: absolute;
    left: 0; top: 992px;
    width: 927px; height: 9px;
    background: var(--band-grey);
  }
  .footer {
    position: absolute;
    left: 0; top: 1001px;
    width: 927px; height: 199px;
    background: linear-gradient(180deg, #151515, var(--black));
  }
  .footer-divider {
    position: absolute;
    left: 390px; top: 1001px;
    width: 1px; height: 199px;
    background: #777;
  }
  .call-now {
    position: absolute;
    left: 16px; top: 1058px;
    margin: 0;
    font-size: 69px;
    font-weight: 400;
    line-height: 1;
    white-space: nowrap;
  }
  .locations {
    position: absolute;
    left: 425px; top: 1066px;
    width: 483px;
    margin: 0; padding: 0;
    list-style: none;
    font-size: 39px;
    line-height: 49px;
  }
  .locations li { display: flex; justify-content: space-between; }
</style>
</head>
<body>
<main class="flyer">
  <div class="side-band"></div>
  <div class="side-rule"></div>
  <div class="side-title">maple lash nook &amp;&nbsp; lash extensions bar</div>

  <h1 class="headline">OVER YOUR BROWS? HAD A DODGE JOB?</h1>

  <p class="service rehab"><strong>&nbsp;Lid Tango:</strong>Our trained<br>staff are here to get your<br>brows back on track! Ser-<br>vice includes: Total brow re-<br>shape,<br>calming forehead and<br>eyebrow Indian massage,<br>soothing rosewater eye gel<br>application, brow finish with<br>complimentary brow<br><span class="on-photo">makeup.</span></p>

  <div class="lash-photo" role="img" aria-label="Close-up photograph of an eye with long lash extensions"></div>

  <p class="service city"><strong>Arches by the Harbour:</strong><br>Perfectly sculpted, arched and<br>groomed? Check! Get the<br>most gorgeous brows ever!<br>Service includes: brow gossip,<br>brow shape, brow colour,<br>calming forehead and<br>eyebrow Indian massage,<br>soothing rosewater eye gel<br>application, and brow finish<br>with complimentary brow<br>makeup.<br>$25.00</p>

  <p class="service teens"><strong>Brows for Teens:</strong> Stand out<br>at school for the right<br>reason! No more<br>mono-brow! Quick,<br>thorough tidy, designed to<br>suit your face. For students<br>up to year<br>12.<br>$14.00</p>

  <p class="service men"><strong>Brows for Men:</strong> Men, let’s<br>be honest. Big Bushy Brows<br>CAN be embarrassing.<br>That’s where we come in. If<br>you’re after a total reshape<br>or just sick of that<br>mono-brow, we’ll give you<br>the look you’re after. There’s<br>never too little or too much<br>we can do to help!<br>$15.00</p>

  <div class="footer-rule"></div>
  <div class="footer"></div>
  <div class="footer-divider"></div>
  <p class="call-now">CALL NOW!</p>
  <ul class="locations">
    <li><span>ASHGROVE</span><span>47261839</span></li>
    <li><span>WILLOWBANKS</span><span>47285106</span></li>
  </ul>
</main>
</body>
</html>
```